Design a Professional Business Card for Vello Marra

Design a business card for Vello Marra, we are a National Sport Court Company.

West Region Address: 4172 Glen Harrow Ct, Suite #210 Englewood, Colorado 80112
East Region Address: 7316 38th Ave W, Bradenton, Florida 34210

Target Market(s)

High End Residential & Institutional Clients

Industry/Entity Type

Design & Construction

Contact Information for Business Card

Logo/Brand/Colors/ name, number (provided in comments)

Requirements
Must have
• Colors only provided in logo
Should not have
• Any other colors not in existing logo (attached)

```html
<!DOCTYPE html>
<html lang="en">
<head>
<meta charset="utf-8">
<title>Vello Marra — Business Card</title>
<link rel="stylesheet" href="https://fonts.googleapis.com/css2?family=Orbitron:wght@700&family=Poppins:wght@400;700&display=swap">
<style>
  :root {
    --navy: #1f3667;
    --green: #006b3a;
    --green-light: #1a8a4e;
    --card-white: #ffffff;
    --ink: #1c1c1c;
    --backdrop: #e7e4df;
  }
  * { margin: 0; padding: 0; box-sizing: border-box; }
  html, body { width: 916px; height: 1200px; overflow: hidden; }
  body { background: var(--backdrop); position: relative; font-family: "Poppins", sans-serif; }

  .card {
    position: absolute;
    left: 72px;
    width: 772px;
    height: 460px;
    border-radius: 27px;
    box-shadow: 0 6px 16px rgba(0,0,0,0.18);
    overflow: hidden;
  }
  .card--front { top: 108px; background: var(--card-white); }
  .card--back  { top: 640px; background: var(--green); }

  .wordmark {
    position: absolute;
    font-family: "Orbitron", sans-serif;
    font-weight: 700;
    line-height: 1;
    letter-spacing: 4px;
    text-transform: uppercase;
  }
  .card--front .wordmark {
    left: 38px; top: 46px;
    font-size: 40px;
    color: var(--navy);
  }
  .wordmark span { display: block; }
  .wordmark span + span { margin-top: 8px; }

  .holder {
    position: absolute;
    right: 51px; top: 58px;
    text-align: right;
  }
  .holder__name {
    font-weight: 700;
    font-size: 25px;
    line-height: 1.1;
    color: var(--navy);
  }
  .holder__name .credential { color: var(--green); }
  .holder__title {
    font-size: 16.5px;
    color: var(--ink);
    margin-top: 3px;
  }

  .brand-disc {
    position: absolute;
    left: 415px; top: 128px;
    width: 306px; height: 306px;
    border-radius: 50%;
    background: var(--green);
  }

  .contacts {
    position: absolute;
    left: 38px; top: 322px;
    list-style: none;
    font-size: 16.5px;
    color: var(--ink);
  }
  .contacts li {
    display: flex; align-items: center;
    height: 25.5px;
  }
  .contacts svg { width: 16px; height: 16px; margin-right: 10px; fill: var(--green); flex: none; }

  .card--back .wordmark {
    left: 296px; top: 203px;
    font-size: 44px;
    color: var(--green-light);
  }
  .card--back .wordmark span + span { margin-top: 12px; }
  .back-disc {
    position: absolute;
    left: 137px; top: 186px;
    width: 134px; height: 134px;
    border-radius: 50%;
    background: var(--green-light);
  }
</style>
</head>
<body>

<section class="card card--front" aria-label="Business card front">
  <div class="wordmark"><span>Vello</span><span>Marra</span></div>

  <div class="holder">
    <p class="holder__name">Dorian J. Whitlock, <span class="credential">ASLA</span></p>
    <p class="holder__title">CEO &amp; Founder</p>
  </div>

  <div class="brand-disc"></div>

  <ul class="contacts">
    <li>
      <svg viewBox="0 0 24 24"><path d="M6.6 10.8a15.1 15.1 0 0 0 6.6 6.6l2.2-2.2a1 1 0 0 1 1-.25 11.4 11.4 0 0 0 3.6.57 1 1 0 0 1 1 1V20a1 1 0 0 1-1 1A17 17 0 0 1 3 4a1 1 0 0 1 1-1h3.5a1 1 0 0 1 1 1c0 1.25.2 2.45.57 3.57a1 1 0 0 1-.25 1z"/></svg>
      (303) 555-0147
    </li>
    <li>
      <svg viewBox="0 0 24 24"><path d="M2 8c0-2 4-4 10-4s10 2 10 4v2h-5V8H7v2H2zM6 12h12l2 8H4zm6 2a2 2 0 1 0 0 4 2 2 0 0 0 0-4z"/></svg>
      1-800-555-0193
    </li>
    <li>
      <svg viewBox="0 0 24 24"><path d="M2 5h20v14H2zm2 2v.5l8 5 8-5V7l-8 5z"/></svg>
      dorian@vellomarraco.com
    </li>
    <li>
      <svg viewBox="0 0 24 24"><path d="M12 2a10 10 0 1 0 0 20 10 10 0 0 0 0-20zm-1 17.9A8 8 0 0 1 4.1 10.5L9 15v1a2 2 0 0 0 2 2zm6.9-2.5A2 2 0 0 0 16 16h-1v-3a1 1 0 0 0-1-1H8v-2h2a1 1 0 0 0 1-1V7h2a2 2 0 0 0 2-2v-.4a8 8 0 0 1 2.9 12.8z"/></svg>
      www.vellomarra.com
    </li>
  </ul>
</section>

<section class="card card--back" aria-label="Business card back">
  <div class="back-disc"></div>
  <div class="wordmark"><span>Vello</span><span>Marra</span></div>
</section>

</body>
</html>
```